Flyer-Design für Segelverein
Zielgruppe
Wir sind ein kleiner Berliner Segelverein im Herzen von Berlin. Unsere Zielgruppe sind wasserbegeisterte Menschen zwischen 20-50 Jahre.
Ein Eindruck über unseren Verein gibt es auf der neuen Webseite (noch im Aufbau): www.wellenrunde-kiel.de
und der alten webseite: www.wellenrundekiel.de
Aufgabenstellung
Wir benötigen den Flyer zum Anwerben neuer Mitglieder. D.h. der Flyer soll alle notwendigen Informationen beinhalten, auf das nötigste reduziert. Vom Format würden wir daher eher was kompaktes sehen (z.b. DIN lang beidseitig bedruckt). Dann könnte auf der Vorderseite die wichtigsten Informationen zum Verein stehen und auf der Rückseite Gründe, Mitglied zu werden.
Zum Verein
1972 gegründet mit dem Ziel, das Seesegeln zu fördern. Die damalige Begeisterung, gemeinsam etwas vollbringen zu können, führte in den Jahren 1975/76 zu einer Folge von Seetörns, bei der ausnahmslos Mitglieder beteiligt waren, von der Ostsee über Norwegen, England, Kanarische Inseln, Karibik über die Bermudas und Azoren wieder zurück in die Ostsee.
Warum der Verein:
- Verkehrsgünstig und zentral gelegen direkt an der Lindgasse - Sehr gut zu erreichen mit den ÖPNVs
- Einzigartiger Schwimmsteg in Berlin ohne Landzugang - Ein Ort zum Verweilen und Abschalten
- verfügbare Stegplätze für Bootsbesitzer
- Viele Vereinsboote für Mitglieder ohne Boot -
- Günstige Mitgliedsbeiträge - Studenten und Schüler erhalten Ermässigungen
- Ein familiärer kleiner Verein - Keine umfangreichen Pflichtarbeiten
- Vereinsinterne Regatten entlang der Havel
- Spannende interne Events und Ausbildungsangebote wie z.b. Fahrten mit dem Dreimast-Gaffelschooner Solvenja, Knotenkurse, Navigation

```html
<!DOCTYPE html>
<html lang="de">
<head>
<meta charset="utf-8">
<title>Warum der Verein?</title>
<link href="https://fonts.googleapis.com/css2?family=Cabin:wght@400;500;600&display=swap" rel="stylesheet">
<style>
  :root {
    --navy-dark: #1f232c;
    --signal-red: #b23f31;
    --card: rgba(255, 255, 255, 0.93);
    --card-first: rgba(240, 240, 240, 0.96);
    --text-navy: #2d3850;
    --white: #ffffff;
    --strip: #2a2d33;
  }
  html, body {
    margin: 0;
    padding: 0;
    width: 856px;
    height: 1200px;
    overflow: hidden;
    background: #ffffff;
  }
  .flyer {
    position: relative;
    width: 856px;
    height: 1200px;
    overflow: hidden;
    font-family: "Cabin", "Gill Sans", sans-serif;
  }
  .header {
    position: absolute;
    left: 0; top: 0;
    width: 856px; height: 165px;
    background: var(--navy-dark);
  }
  .header h1 {
    position: absolute;
    left: 36px; top: 30px;
    margin: 0;
    color: var(--white);
    font-weight: 500;
    font-size: 76px;
    letter-spacing: -1px;
    line-height: 1;
  }
  .accent-band {
    position: absolute;
    left: 0; top: 165px;
    width: 856px; height: 33px;
    background: var(--signal-red);
  }
  .hero-photo {
    position: absolute;
    left: 0; top: 198px;
    width: 856px; height: 805px;
    background:
      radial-gradient(ellipse at 70% 60%, rgba(180, 190, 205, 0.55), transparent 55%),
      radial-gradient(ellipse at 20% 20%, rgba(150, 165, 190, 0.5), transparent 60%),
      linear-gradient(160deg, #6d7b93 0%, #3e4b63 45%, #2b3346 75%, #1e232e 100%);
  }
  .reasons {
    position: absolute;
    left: 49px; top: 253px;
    margin: 0; padding: 0;
    list-style: none;
  }
  .reason {
    width: 758px;
    height: 67px;
    margin-bottom: 22.5px;
    background: var(--card);
    color: var(--text-navy);
    font-size: 36px;
    font-weight: 500;
    line-height: 67px;
    padding-left: 7px;
    box-sizing: border-box;
    white-space: nowrap;
    letter-spacing: -0.2px;
  }
  .reason:first-child { background: var(--card-first); }
  .dark-strip {
    position: absolute;
    left: 0; top: 1003px;
    width: 856px; height: 32px;
    background: var(--strip);
  }
  .contact {
    position: absolute;
    left: 0; top: 1035px;
    width: 856px; height: 165px;
    background: var(--signal-red);
    color: var(--white);
  }
  .contact h2 {
    position: absolute;
    left: 34px; top: 8px;
    margin: 0;
    font-size: 40px;
    font-weight: 500;
  }
  .contact-item {
    position: absolute;
    display: flex;
    align-items: center;
    font-size: 23px;
    font-weight: 500;
    white-space: nowrap;
  }
  .contact-icon {
    width: 43px; height: 43px;
    border-radius: 50%;
    background: var(--white);
    display: flex;
    align-items: center;
    justify-content: center;
    margin-right: 16px;
    flex: none;
  }
  .contact-icon svg { width: 24px; height: 24px; }
  .item-address { left: 36px; top: 55px; }
  .item-phone   { left: 36px; top: 113px; }
  .item-mail    { left: 441px; top: 54px; }
  .item-web     { left: 441px; top: 113px; }
  .item-mail .contact-icon, .item-web .contact-icon { margin-right: 11px; }
</style>
</head>
<body>
<div class="flyer">
  <header class="header">
    <h1>Warum der Verein?</h1>
  </header>
  <div class="accent-band"></div>

  <div class="hero-photo" role="img" aria-label="Nahaufnahme einer Segelboot-Winsch mit weiß-blauem Tauwerk"></div>

  <ul class="reasons">
    <li class="reason">- Zentrale Lage (gut zu erreichen, ÖPNV)</li>
    <li class="reason">- Einzigartiger Schwimmsteg in Berlin</li>
    <li class="reason">- Verfügbare Stegplätze für Bootsbesitzer</li>
    <li class="reason">- Viele Vereinsboote für Mitglieder</li>
    <li class="reason">- Günstige Mitgliedsbeiträge</li>
    <li class="reason">- Keine umfangreichen Pflichtarbeiten</li>
    <li class="reason">- Vereinsinterne Regatten entlang der Havel</li>
    <li class="reason">- Interne Events &amp; Ausbildungsmöglichkeiten</li>
  </ul>

  <div class="dark-strip"></div>

  <footer class="contact">
    <h2>Kontakt</h2>

    <div class="contact-item item-address">
      <span class="contact-icon">
        <svg viewBox="0 0 24 24" fill="none" stroke="#b23f31" stroke-width="1.8">
          <path d="M12 22s-7-7.2-7-12.5A7 7 0 0 1 19 9.5C19 14.8 12 22 12 22z"/>
          <circle cx="12" cy="9.5" r="2.6"/>
        </svg>
      </span>
      Am Wellenufer 7, 13595 Berlin
    </div>

    <div class="contact-item item-phone">
      <span class="contact-icon">
        <svg viewBox="0 0 24 24" fill="#b23f31">
          <path d="M6.6 2.5l3 3.6-1.8 2.4c1.2 2.6 3.1 4.5 5.7 5.7l2.4-1.8 3.6 3-1.6 3.6c-.5.6-1.3.9-2.1.7C9.4 18.2 5.8 14.6 4.3 8.2c-.2-.8.1-1.6.7-2.1z"/>
        </svg>
      </span>
      +49 &nbsp;(030) 555 01 23
    </div>

    <div class="contact-item item-mail">
      <span class="contact-icon">
        <svg viewBox="0 0 24 24" fill="none" stroke="#b23f31" stroke-width="1.8">
          <rect x="3" y="6" width="18" height="12" rx="1"/>
          <path d="M3 6l9 7 9-7M3 18l7-6M21 18l-7-6"/>
        </svg>
      </span>
      info@wellenrunde-kiel.de
    </div>

    <div class="contact-item item-web">
      <span class="contact-icon">
        <svg viewBox="0 0 24 24" fill="none" stroke="#b23f31" stroke-width="1.5">
          <circle cx="12" cy="12" r="9"/>
          <ellipse cx="12" cy="12" rx="4" ry="9"/>
          <path d="M3 12h18M4.5 7.5h15M4.5 16.5h15"/>
        </svg>
      </span>
      www.wellenrunde-kiel.de
    </div>
  </footer>
</div>
</body>
</html>
```